Music Industry Business Needs a Business Card Design

Copper Lantern is an audio mastering company that has been in business for 20 years. Mastering is the final creative step in the music production chain. Our job is to make the music sound as good as it possibly can prior to release to the public. Our world is technical, artistic, precise. We work on everything from independent artists to the music for the Grandfield Cup. We are looking for a new, more modern business card design. I am uploading a copy of our logo, although it doesn't absolutely need to be included in the design.

Target Market(s)

Music Industry Professionals

Industry/Entity Type

Business

Contact Information for Business Card

Address, Phone, Email, Website, Name, Job Title

Font styles to use
Sans Serif

Requirements
Must have
• Sorry, but I don't have any concrete things to request. If I had a clear idea of what I want, I would probably just design something myself. I am looking for fresh input and thought I would try this.
Should not have
• Anything that is typical, such as headphones or the like.

```html
<!DOCTYPE html>
<html lang="en">
<head>
<meta charset="utf-8">
<title>Copper Lantern – Business Card</title>
<link href="https://fonts.googleapis.com/css2?family=Jost:wght@400;500;600&display=swap" rel="stylesheet">
<style>
  :root {
    --canvas-bg: #d4d8d4;
    --card-dark: #161718;
    --card-dark-sheen: #3a3d40;
    --card-white: #ffffff;
    --accent-green: #7dff0a;
    --text-dark: #1e1e1e;
    --text-grey: #cfcfcf;
  }
  * { margin: 0; padding: 0; box-sizing: border-box; }
  html, body {
    width: 1200px;
    height: 1000px;
    overflow: hidden;
    background: var(--canvas-bg);
    font-family: "Jost", "Century Gothic", sans-serif;
  }
  .business-card {
    position: absolute;
    left: 75px;
    top: 200px;
    width: 1050px;
    height: 600px;
    box-shadow: 0 14px 40px rgba(0,0,0,0.35);
    overflow: hidden;
  }
  .card-shapes {
    position: absolute;
    inset: 0;
    width: 100%;
    height: 100%;
  }
  .brand {
    position: absolute;
    left: 330px;
    top: 62px;
    display: flex;
    align-items: center;
    gap: 14px;
    color: var(--accent-green);
    font-size: 34px;
    font-weight: 400;
    letter-spacing: 1px;
    text-transform: uppercase;
  }
  .brand-dot {
    width: 18px;
    height: 18px;
    border-radius: 50%;
    background: var(--accent-green);
  }
  .person {
    position: absolute;
    left: 690px;
    top: 262px;
  }
  .person-name {
    color: var(--accent-green);
    font-size: 52px;
    font-weight: 600;
    line-height: 1;
  }
  .person-title {
    color: var(--text-grey);
    font-size: 34px;
    font-weight: 400;
    margin-top: 6px;
    margin-left: 4px;
  }
  .contact-list {
    position: absolute;
    left: 230px;
    top: 268px;
    list-style: none;
    color: var(--text-dark);
    font-size: 38px;
    font-weight: 500;
    line-height: 1.15;
  }
  .contact-list .email { font-size: 34px; }
  .website {
    position: absolute;
    left: 90px;
    top: 503px;
    color: var(--card-white);
    font-size: 56px;
    font-weight: 500;
    letter-spacing: 1px;
  }
</style>
</head>
<body>
  <section class="business-card" aria-label="Copper Lantern business card">
    <svg class="card-shapes" viewBox="0 0 1050 600" preserveAspectRatio="none" aria-hidden="true">
      <defs>
        <linearGradient id="darkPanel" x1="0" y1="0" x2="1" y2="1">
          <stop offset="0" stop-color="var(--card-dark)"/>
          <stop offset="0.45" stop-color="var(--card-dark-sheen)"/>
          <stop offset="1" stop-color="var(--card-dark)"/>
        </linearGradient>
      </defs>
      <rect class="white-field" width="1050" height="600" fill="var(--card-white)"/>
      <path class="dark-panel" d="M0 0 H1050 V455 C760 300 320 190 0 150 Z" fill="url(#darkPanel)"/>
      <path class="accent-curve" d="M0 150 C320 190 760 300 1050 455" fill="none" stroke="var(--accent-green)" stroke-width="5"/>
      <rect class="web-band" x="0" y="490" width="1050" height="110" fill="var(--accent-green)"/>
    </svg>

    <div class="brand"><span class="brand-dot"></span>Copper Lantern</div>

    <div class="person">
      <p class="person-name">Alex Carter</p>
      <p class="person-title">manager</p>
    </div>

    <ul class="contact-list">
      <li class="phone">555 410 2786</li>
      <li class="address">48 Harbor Row</li>
      <li class="email">info@copperlantern.com</li>
    </ul>

    <p class="website">www.copperlantern.com</p>
  </section>
</body>
</html>
```